Business Card Design - Construction Company

Torvane Construction is in need of a sharp, modern business card design that has an architectural/high fashion feel.

We are looking for a two sided card.

One side simple dark grey/black with some texture in the background. e.g. (a mosaic of simple interconnecting shapes or a shadow of the logo.) Something to draw attention and create interest.It will need to feature a large Torvane construction logo (files attached) in metallic gradient or plain white.

The other side should contain all of our information:

(in largest text)
Name of person
Torvane Construction Pty. Ltd.

Licensed builders specialising in:
- Bathrooms
- Kitchens
- Commercial interiors

(mid sized text)
Phone number
Fax number
person@torvaneconstruction.example.au
www. torvaneconstruction.example.au

(smaller text)
ABN: 47209836512
BSA license: xxx-xxxx
PO Box 8640 Dunmore QLD 4170 (address)

Target Market(s)

professional home and business owners

Industry/Entity Type

Construction

Requirements
Must have
• Must be bold, professional looking and modern.
Nice to have
• We are undecided as to what kind of printing we will go with.
Definitely square edged.
Probably high quality satin card.
We are also interested in designs that would work well on transparent or translucent plastic.
Ideally we would print two versions.
Should not have
• Nothing with an antique feel.
No wild colours. Small amounts of colour can be good in the right place.

```html
<!DOCTYPE html>
<html lang="en">
<head>
<meta charset="utf-8">
<title>Business Card Design for Torvane Construction</title>
<link rel="stylesheet" href="https://fonts.googleapis.com/css2?family=Archivo+Narrow:wght@400;700&family=Fira+Sans+Extra+Condensed:wght@300&family=Montserrat:wght@600&family=Arimo&display=swap">
<style>
  :root {
    --board-light: #f1f1f1;
    --board-dark: #d4d4d4;
    --card-black: #1f1d1c;
    --card-deep: #141312;
    --header-blue: #1f5db8;
    --header-blue-dark: #123f86;
    --list-blue: #8ec6f0;
    --white: #ffffff;
    --fine-grey: #8a8a8a;
    --metal: #c8c8c8;
    --label-blue: #4a5278;
    --label-dark: #222222;
    --label-grey: #8c8c8c;
    --rule: #a8a8a8;
  }
  * { margin: 0; padding: 0; box-sizing: border-box; }
  html, body { width: 1200px; height: 846px; overflow: hidden; }
  body {
    position: relative;
    background: radial-gradient(ellipse at 45% 40%, var(--board-light) 0%, var(--board-dark) 100%);
    font-family: "Archivo Narrow", "Arial Narrow", sans-serif;
  }
  .card {
    position: absolute;
    top: 175px;
    width: 289px;
    height: 508px;
    background: linear-gradient(180deg, var(--card-black) 0%, var(--card-deep) 100%);
    box-shadow: 3px 4px 8px rgba(0,0,0,0.35);
    overflow: hidden;
  }
  .card--info { left: 102px; }
  .card--brand { left: 452px; }

  /* info side */
  .company-band {
    position: absolute;
    left: 35px; top: 0;
    width: 221px; height: 84px;
    background: linear-gradient(180deg, var(--header-blue) 0%, var(--header-blue-dark) 100%);
    color: var(--white);
    font-family: "Montserrat", sans-serif;
    font-weight: 600;
  }
  .company-name { position: absolute; left: 14px; top: 41px; font-size: 15px; letter-spacing: 1.6px; line-height: 1; }
  .company-suffix { position: absolute; left: 14px; top: 63px; font-size: 9.5px; letter-spacing: 1.4px; line-height: 1; }

  .services { position: absolute; left: 47px; top: 102px; font-size: 12.5px; line-height: 16.5px; }
  .services-lead { color: var(--white); font-weight: 700; }
  .services-list { list-style: none; color: var(--list-blue); font-weight: 700; }

  .mark-band {
    position: absolute; left: 0; top: 190px; width: 289px; height: 76px;
    background: linear-gradient(180deg, rgba(255,255,255,0) 0%, rgba(255,255,255,0.05) 50%, rgba(255,255,255,0) 100%);
  }

  .person { position: absolute; left: 45px; top: 308px; color: var(--white); font-weight: 700; font-size: 23px; line-height: 1; }
  .contact { position: absolute; left: 45px; top: 344px; list-style: none; color: var(--white); font-size: 11.5px; line-height: 17.3px; }
  .contact-key { display: inline-block; width: 21px; }
  .legal { position: absolute; left: 44px; top: 440px; list-style: none; color: var(--fine-grey); font-family: "Arimo", Arial, sans-serif; font-size: 8px; line-height: 15px; }

  /* brand side */
  .texture {
    position: absolute; inset: 0;
    background: radial-gradient(circle at 50% 48%, #2a2827 0%, #1b1a19 70%, #131211 100%);
  }
  .brand-ring {
    position: absolute; left: 117px; top: 203px; width: 56px; height: 56px;
    border: 4px solid var(--metal); border-radius: 50%;
  }
  .brand-name {
    position: absolute; left: 0; width: 289px; text-align: center;
    color: var(--metal); font-family: "Montserrat", sans-serif; font-weight: 600; line-height: 1;
  }
  .brand-name--main { top: 303px; font-size: 24px; letter-spacing: 1.5px; }
  .brand-name--sub { top: 326px; font-size: 8.5px; letter-spacing: 1.8px; }

  /* presentation labels */
  .rule { position: absolute; left: 815px; width: 318px; height: 2px; background: var(--rule); }
  .rule--top { top: 177px; }
  .rule--mid { top: 299px; }
  .board-label { position: absolute; font-family: "Fira Sans Extra Condensed", sans-serif; font-weight: 300; line-height: 1; }
  .board-label--intro { left: 821px; top: 197px; font-size: 28px; color: var(--label-blue); }
  .board-label--intro small { font-size: 18px; }
  .board-label--client { left: 820px; top: 240px; font-size: 41px; color: var(--label-dark); }
  .board-label--variant { left: 820px; top: 648px; font-size: 40px; color: var(--label-grey); }
</style>
</head>
<body>
  <section class="card card--info" aria-label="Card information side">
    <header class="company-band">
      <div class="company-name">TORVANE</div>
      <div class="company-suffix">CONSTRUCTION PTY. LTD.</div>
    </header>
    <div class="services">
      <p class="services-lead">Licensed builders specialising in:</p>
      <ul class="services-list">
        <li>- Bathrooms</li>
        <li>- Kitchens</li>
        <li>- Commercial interiors</li>
      </ul>
    </div>
    <div class="mark-band" role="img" aria-label="Faint row of the company symbol as background decoration"></div>
    <h1 class="person">John Doe</h1>
    <ul class="contact">
      <li><span class="contact-key">{P}</span>0491 5702 36</li>
      <li><span class="contact-key">{F}</span>0755 5018 42</li>
      <li><span class="contact-key">{E}</span>person@torvaneconstruction.example.au</li>
      <li><span class="contact-key">{W}</span>www. torvaneconstruction.example.au</li>
    </ul>
    <ul class="legal">
      <li>ABN: 47209836512</li>
      <li>BSA license: xxx-xxxx</li>
      <li>PO Box 8640 Dunmore QLD 4170</li>
    </ul>
  </section>

  <section class="card card--brand" aria-label="Card brand side">
    <div class="texture" role="img" aria-label="Dark tiled pattern of the company symbol"></div>
    <div class="brand-ring"></div>
    <div class="brand-name brand-name--main">TORVANE</div>
    <div class="brand-name brand-name--sub">CONSTRUCTION</div>
  </section>

  <div class="rule rule--top"></div>
  <p class="board-label board-label--intro">Business Card Design <small>for</small></p>
  <p class="board-label board-label--client">Torvane Construction</p>
  <div class="rule rule--mid"></div>
  <p class="board-label board-label--variant">Type B - i</p>
</body>
</html>
```